Wireless Broadband Newspaper AD

We have recently re-branded our company, new logo and website.

Our primary product offering is Wireless Broadband services to region, the target audience generally cannot get ADSL broadband.

We wanted to pose the question "Can't get ADSL ?" to attract the attention of those who are unable to access conventional mass market broadband offerings.

Ad Size should be:
129mm Wide
178mm High

Please find the text for the AD below.

Can't get ADSL ?
Try Fixed Wireless Broadband

* Speeds up to 10Mbit
* Plans from $29.95 per month
* Up to 60GB Download Allowance
* $99 Professional On-site Installation
* No Contracts

http://pelnetlink.com.au
CALL NOW - 1300 47 91 63

-

Target Market(s)

Frequent Internet users, requiring broadband access in their homes.

Industry/Entity Type

It Company

Requirements
Must have
• Ensure that the general branding feel of the existing website is considered, please us similar colours and theme.
• As well as our logo, which you will find attached in EPS format.
• http://pelnetlink.com.au
Nice to have
• Large caption "Can't get ADSL?"

```html
<!DOCTYPE html>
<html lang="en">
<head>
<meta charset="utf-8">
<title>Pelnet Link – Can't get ADSL?</title>
<link rel="stylesheet" href="https://fonts.googleapis.com/css2?family=Orbitron:wght@700;800&family=PT+Sans:wght@400;700&display=swap">
<style>
  :root {
    --stage: #000000;
    --card-top: #f4f4f4;
    --card-bottom: #d9d9d9;
    --orange-light: #fbb02c;
    --orange-mid: #f7941d;
    --orange-deep: #f37a20;
    --ink: #1a1a1a;
    --white: #ffffff;
    --grey-text: #5a5a5a;
    --brand-grey: #3b3b3b;
  }
  * { margin: 0; padding: 0; box-sizing: border-box; }
  html, body {
    width: 1200px; height: 900px; overflow: hidden;
    background: var(--stage);
  }
  .canvas { position: relative; width: 1200px; height: 900px; }
  .ad {
    position: absolute; left: 274px; top: 30px;
    width: 652px; height: 840px;
    background: linear-gradient(180deg, var(--card-top), var(--card-bottom));
    font-family: "PT Sans", Arial, sans-serif;
  }
  .brand {
    position: absolute; left: 44px; top: 62px;
    display: flex; align-items: center; gap: 14px;
  }
  .brand-dot {
    width: 46px; height: 46px; border-radius: 50%;
    background: var(--orange-mid);
  }
  .brand-name {
    font-weight: 700; font-size: 46px; color: var(--brand-grey);
    letter-spacing: -0.5px; line-height: 1;
  }
  .offer {
    position: absolute; left: 26px; top: 160px;
    width: 604px; height: 620px; border-radius: 16px;
    background: linear-gradient(100deg, var(--orange-light) 0%, var(--orange-mid) 55%, var(--orange-deep) 100%);
    color: var(--white);
  }
  .question-lead {
    position: absolute; left: 30px; top: 42px;
    font-weight: 700; font-size: 46px; color: var(--ink);
    letter-spacing: -1px; line-height: 1;
  }
  .question-main {
    position: absolute; left: 28px; top: 96px;
    font-family: "Orbitron", "Arial Black", sans-serif;
    font-weight: 800; font-size: 100px; line-height: 1;
    letter-spacing: 4px;
  }
  .pitch {
    position: absolute; left: 20px; top: 238px;
    font-weight: 700; font-size: 34px; color: var(--ink);
    letter-spacing: -0.3px;
  }
  .features {
    position: absolute; left: 44px; top: 300px;
    list-style: none;
  }
  .features li {
    position: relative; padding-left: 26px;
    font-size: 25px; line-height: 34.5px;
  }
  .features li::before {
    content: ""; position: absolute; left: 0; top: 10px;
    width: 14px; height: 14px; background: var(--white);
  }
  .call-label {
    position: absolute; left: 24px; top: 476px;
    font-weight: 700; font-size: 38px; color: var(--ink);
    letter-spacing: -1px; line-height: 1;
  }
  .phone {
    position: absolute; left: 22px; top: 522px;
    font-family: "Orbitron", "Arial Black", sans-serif;
    font-weight: 800; font-size: 62px; line-height: 1;
    letter-spacing: 1px; white-space: nowrap;
  }
  .website {
    position: absolute; left: 0; right: 0; top: 792px;
    text-align: center; font-size: 24px; color: var(--grey-text);
  }
</style>
</head>
<body>
<div class="canvas">
  <article class="ad">
    <div class="brand">
      <span class="brand-dot"></span>
      <span class="brand-name">pelnetlink</span>
    </div>
    <section class="offer">
      <p class="question-lead">Can’t get</p>
      <h1 class="question-main">ADSL ?</h1>
      <h2 class="pitch">Try Fixed Wireless Broadband</h2>
      <ul class="features">
        <li>Speeds up to 10Mbit</li>
        <li>Plans from $29.95 per month</li>
        <li>Up to 60GB Download Allowance</li>
        <li>$99 Professional On-site Installation</li>
        <li>No Contracts</li>
      </ul>
      <p class="call-label">Call NOW</p>
      <p class="phone">1300 47 91 63</p>
    </section>
    <p class="website">www.pelnetlink.com.au</p>
  </article>
</div>
</body>
</html>
```